Vorapo Business Card

Need a double sided business card. Would like the business card to have the logo on one side and the employees details and business contact details on the other.

Business

```html
<!DOCTYPE html>
<html lang="en">
<head>
<meta charset="utf-8">
<title>Vorapo Business Card</title>
<link rel="stylesheet" href="https://fonts.googleapis.com/css2?family=Open+Sans:wght@400;600;700&display=swap">
<style>
  :root {
    --backdrop: #e9e8e6;
    --card-dark: #202020;
    --card-back: #1b1b1b;
    --emboss: #2b2b2b;
    --emboss-soft: #262626;
    --lime: #8dc63f;
    --text-light: #b9bcbf;
    --text-muted: #8a8d90;
    --band-grey: #a4abb2;
    --divider: #55585b;
  }
  * { margin: 0; padding: 0; box-sizing: border-box; }
  html, body {
    width: 1200px;
    height: 716px;
    overflow: hidden;
    background: var(--backdrop);
    font-family: "Open Sans", Arial, sans-serif;
  }
  .stage {
    position: relative;
    width: 1200px;
    height: 716px;
  }
  .card {
    position: absolute;
    top: 204px;
    width: 540px;
    height: 309px;
    overflow: hidden;
    box-shadow: 0 6px 18px rgba(0,0,0,0.25);
  }

  /* Back side: logo only */
  .card-back {
    left: 40px;
    background: var(--card-back);
  }
  .card-back .wordmark {
    position: absolute;
    left: 52px;
    top: 92px;
    font-size: 84px;
    font-weight: 700;
    letter-spacing: -1px;
    color: var(--emboss);
    line-height: 1;
  }
  .card-back .mark-square {
    position: absolute;
    right: 58px;
    top: 70px;
    width: 150px;
    height: 150px;
    border-radius: 14px;
    background: var(--emboss-soft);
  }

  /* Front side: details */
  .card-front {
    left: 620px;
    background: var(--card-dark);
  }
  .card-front .mark-square {
    position: absolute;
    right: 34px;
    top: 150px;
    width: 120px;
    height: 120px;
    border-radius: 12px;
    background: #272727;
  }
  .brand {
    position: absolute;
    left: 34px;
    top: 28px;
    font-size: 64px;
    font-weight: 700;
    letter-spacing: -1px;
    color: var(--lime);
    line-height: 1;
  }
  .person {
    position: absolute;
    left: 38px;
    top: 104px;
  }
  .person-name {
    font-size: 13px;
    font-weight: 700;
    color: var(--lime);
  }
  .person-title {
    font-size: 11px;
    color: var(--text-muted);
  }
  .contact-list {
    position: absolute;
    left: 38px;
    top: 160px;
    list-style: none;
  }
  .contact-list li,
  .location li {
    display: flex;
    align-items: center;
    gap: 7px;
    font-size: 11.5px;
    color: var(--text-light);
    line-height: 1.6;
  }
  .icon {
    width: 11px;
    height: 11px;
    flex: none;
  }
  .location {
    position: absolute;
    left: 292px;
    top: 208px;
    padding-left: 14px;
    border-left: 1px solid var(--divider);
    list-style: none;
  }
  .location li { align-items: flex-start; }
  .location .icon { margin-top: 3px; }
  .location .web {
    font-weight: 700;
    color: #d4d6d8;
  }
  .base-band {
    position: absolute;
    left: 0;
    right: 0;
    bottom: 0;
    height: 14px;
    background: var(--band-grey);
    border-top: 2px solid #6c7278;
  }
</style>
</head>
<body>
<main class="stage">

  <section class="card card-back" aria-label="Business card back">
    <div class="mark-square"></div>
    <div class="wordmark">Vorapo</div>
  </section>

  <section class="card card-front" aria-label="Business card front">
    <div class="mark-square"></div>
    <div class="brand">Vorapo</div>

    <div class="person">
      <p class="person-name">Employee Name</p>
      <p class="person-title">Title</p>
    </div>

    <ul class="contact-list">
      <li>
        <svg class="icon" viewBox="0 0 12 12"><circle cx="6" cy="6" r="5.3" fill="none" stroke="#8dc63f" stroke-width="1.2"/><path d="M4 3.5l1 1.4-.6.6a4 4 0 0 0 2 2l.6-.6 1.4 1-.7.8C5.6 8.5 3.6 6.4 3.4 4.3z" fill="#8dc63f"/></svg>
        123 456 8888
      </li>
      <li>
        <svg class="icon" viewBox="0 0 12 12"><circle cx="6" cy="6" r="5.3" fill="none" stroke="#8dc63f" stroke-width="1.2"/><rect x="4.3" y="3" width="3.4" height="6" rx="0.6" fill="#8dc63f"/></svg>
        123 456 5555
      </li>
      <li>
        <svg class="icon" viewBox="0 0 12 12"><circle cx="6" cy="6" r="5.3" fill="none" stroke="#8dc63f" stroke-width="1.2"/><rect x="3.2" y="4" width="5.6" height="4" fill="#8dc63f"/><path d="M3.2 4l2.8 2.2L8.8 4" fill="none" stroke="#202020" stroke-width="0.7"/></svg>
        info@website.com
      </li>
    </ul>

    <ul class="location">
      <li>
        <svg class="icon" viewBox="0 0 12 12"><circle cx="6" cy="6" r="5.3" fill="none" stroke="#8dc63f" stroke-width="1.2"/><path d="M6 2.8a2 2 0 0 1 2 2c0 1.5-2 4-2 4s-2-2.5-2-4a2 2 0 0 1 2-2z" fill="#8dc63f"/></svg>
        <span>Street name, city name,<br>zip code with country</span>
      </li>
      <li>
        <svg class="icon" viewBox="0 0 12 12"><circle cx="6" cy="6" r="5.3" fill="none" stroke="#8dc63f" stroke-width="1.2"/><circle cx="6" cy="6" r="2.8" fill="none" stroke="#8dc63f" stroke-width="0.9"/><path d="M3.2 6h5.6M6 3.2v5.6" stroke="#8dc63f" stroke-width="0.7"/></svg>
        <span class="web">www.website.com</span>
      </li>
    </ul>

    <div class="base-band"></div>
  </section>

</main>
</body>
</html>
```